依頼詳細
ページに使用したいキャッチフレーズ:
個性的な道を究め、劇的に生きる人生を選択する
それがMoonhollow

参考にしたいURL:
https://www.kenmori-ux.brelo.jp/
https://www.sorimachikeigo.com/member-lounge

ムーンホロウクラブのHP:
https://www.ruvo.co.jp/moonhollow/

ページに使用したいテキスト:
『Moonhollow Clubとは

「あなたの好きなことは何ですか?」
好きなことを徹底追求し、“好き”を個性に。
そして、個性を武器にしながら“才能”へと伸ばしていくことで、
人生の構想力が磨かれ、あなたの人生は切り拓かれていきます。

誰かに敷かれたレールに乗りたいのか?
型にはまらない人生を創造したいのか?
一度きりの人生を、自分はどう生きたいか?

「自分らしい」人生を実現しよう!。』

採択後、デザインに利用した、デザインデータもお送りください。
(特に、画像ファイルは必ず送ってください)

何かご不明な点がございましたら、お気軽にお申し付けください。

※ 過去の制作実績をそのままご提案いただいたり、他社のポートフォリオをそのまま掲載することは恐れ入りますが、ご遠慮いただけますと幸いです。
サイトURL
http://moonhollowclub.jp
ページ数
1ページ
希望イメージ
シンプル 複雑
単色 カラフル
暗い 明るい
日常 高級
遊び心 厳粛
未来的 伝統的
女性的 男性的
希望する色
赤系、黄・オレンジ系、ジェンダーニュートラルなデザイン
納品ファイル
• イラストレーター形式 (.ai)
• PNG形式 (.png)
補足説明
デザインに利用した、デザインデータ(画像など)もお送り頂きますようお願い致します。

素晴らしいデザインをありがとうございました。

素晴らしいデザインをありがとうございました。

```html
<!DOCTYPE html>
<html lang="ja">
<head>
<meta charset="utf-8">
<title>Moonhollow Club</title>
<link rel="stylesheet" href="https://fonts.googleapis.com/css2?family=Noto+Sans+JP:wght@400;500;700;900&family=Montserrat:wght@500;700;800&display=swap">
<style>
:root{
  --red:#e8352b;
  --orange:#f57a2a;
  --yellow:#fbc531;
  --ink:#2b2b2b;
  --mute:#8a8a8a;
  --bg:#f1f2f6;
  --card:#ffffff;
  --line:#e3e4ea;
}
*{box-sizing:border-box;margin:0;padding:0}
html,body{width:1200px;height:4784px;overflow:hidden}
body{background:var(--bg);font-family:"Noto Sans JP",sans-serif;color:var(--ink);position:relative}
.abs{position:absolute}
.en{font-family:"Montserrat",sans-serif}

/* header */
.site-header{top:0;left:0;width:1200px;height:64px;background:#fff;display:flex;align-items:center;padding:0 40px;box-shadow:0 2px 8px rgba(0,0,0,.05);z-index:5}
.brand{font-weight:900;font-size:19px;color:var(--ink);display:flex;align-items:center;gap:8px}
.brand-dot{width:12px;height:12px;border-radius:50%;background:var(--red)}
.gnav{margin-left:auto;display:flex;gap:26px;font-size:11px;color:#555}
.gnav .on{color:var(--red);font-weight:700}
.hbtn{margin-left:22px;height:32px;padding:0 18px;border-radius:16px;font-size:11px;font-weight:700;display:flex;align-items:center;color:#fff}
.hbtn.login{background:linear-gradient(90deg,var(--orange),var(--yellow));margin-left:24px}
.hbtn.join{background:linear-gradient(90deg,var(--red),var(--orange));margin-left:10px}

/* hero */
.hero-ring{top:-120px;left:430px;width:760px;height:760px}
.catch{top:250px;left:120px}
.catch p{font-size:30px;font-weight:700;letter-spacing:.06em;line-height:1.55}
.catch .big{font-size:42px;color:var(--red)}
.catch .brand-line{font-size:42px;font-weight:800;letter-spacing:.08em}
.catch .brand-line b{color:var(--red);font-family:"Montserrat",sans-serif}
.photo{border-radius:2px}
.dream{top:815px;left:120px;font-size:60px;font-weight:700;color:#fff;letter-spacing:.02em;text-shadow:0 2px 10px rgba(0,0,0,.15)}

/* about */
.about{top:1160px;left:120px;width:960px;height:840px;background:var(--card);border-radius:6px;box-shadow:0 6px 24px rgba(0,0,0,.05);overflow:hidden;text-align:center}
.about h2{margin-top:96px;font-size:36px;font-weight:800;letter-spacing:.06em}
.about h2 .en{color:var(--red)}
.about h2 .en span{color:var(--ink)}
.bubble{display:inline-block;margin-top:38px;padding:12px 30px;border:2px solid var(--ink);border-radius:4px;font-size:20px;font-weight:700;position:relative}
.bubble em{font-style:normal;color:var(--red)}
.bubble:after{content:"";position:absolute;left:50%;bottom:-10px;width:14px;height:14px;background:#fff;border-right:2px solid var(--ink);border-bottom:2px solid var(--ink);transform:translateX(-50%) rotate(45deg)}
.about .lead{margin-top:40px;font-size:13px;line-height:2.2;color:#444}
.about .lead+.lead{margin-top:20px}
.claim{display:inline-block;margin-top:30px;font-size:24px;font-weight:900;padding:4px 10px;background:linear-gradient(transparent 60%,#ffe27a 60%)}
.btn{display:inline-flex;align-items:center;justify-content:center;gap:8px;height:44px;padding:0 32px;border-radius:22px;font-size:13px;font-weight:700;color:#fff;background:linear-gradient(90deg,var(--red),var(--orange));box-shadow:0 4px 10px rgba(232,53,43,.25)}
.btn.ghost{background:#fff;color:var(--red);border:1.5px solid var(--red);box-shadow:none}
.about .btn{margin-top:34px}
.city{left:0;bottom:0;width:960px;height:170px;background:linear-gradient(0deg,#f7b9a9 0%,#fde1d5 70%,rgba(255,255,255,0) 100%)}

/* quick nav */
.quick{top:2060px;left:120px;width:960px;display:grid;grid-template-columns:1fr 1fr;gap:28px 20px}
.quick a{height:90px;background:#fff;border-radius:4px;display:flex;align-items:center;padding:0 24px;font-size:15px;font-weight:700;color:var(--ink);text-decoration:none;box-shadow:0 3px 12px rgba(0,0,0,.04)}
.quick .ic{width:30px;height:22px;border:2px solid var(--red);border-radius:3px;margin-right:18px}
.quick .go{margin-left:auto;width:22px;height:22px;border-radius:50%;background:var(--red);position:relative}
.quick .go:after,.q .go:after{content:"";position:absolute;left:7px;top:8px;width:5px;height:5px;border-top:2px solid #fff;border-right:2px solid #fff;transform:rotate(45deg)}

/* sections */
.sec-title{font-size:44px;font-weight:800;color:var(--red)}
.sec-title small{font-family:"Noto Sans JP",sans-serif;font-size:13px;color:var(--ink);margin-left:14px;font-weight:500}
.arrows{top:2410px;left:1010px;display:flex;gap:12px}
.arrows span{width:48px;height:48px;border-radius:50%;display:flex;align-items:center;justify-content:center;color:#fff;font-size:18px}
.arrows .prev{background:var(--red)}
.arrows .next{background:#fff;color:var(--red);border:1.5px solid var(--red)}
.movies{top:2500px;left:60px;display:flex;gap:18px}
.mcard{width:320px;height:290px;background:#fff;border-radius:4px;overflow:hidden;box-shadow:0 3px 12px rgba(0,0,0,.05)}
.mthumb{height:170px;background:linear-gradient(135deg,#8a7f86,#c9b7ad);position:relative}
.mthumb .tag{position:absolute;left:10px;top:10px;background:var(--red);color:#fff;font-size:10px;padding:3px 10px;border-radius:2px}
.mthumb .play{position:absolute;left:50%;top:50%;width:50px;height:50px;margin:-25px;border-radius:50%;background:rgba(255,255,255,.85)}
.mthumb .play:after{content:"";position:absolute;left:20px;top:15px;border-left:14px solid var(--red);border-top:10px solid transparent;border-bottom:10px solid transparent}
.mbody{padding:12px 14px;font-size:11px}
.mbody .cat{color:var(--red);font-size:10px}
.mbody .ttl{margin-top:6px;line-height:1.6;font-weight:500}
.mbody .meta{margin-top:10px;display:flex;gap:12px;color:var(--mute);font-size:10px}
.mbody .meta i{display:inline-block;width:18px;height:18px;border-radius:50%;background:#ddd;vertical-align:middle;margin-right:4px}

.blog-head{top:3020px;left:0;width:1200px;text-align:center}
.blog-head .sec-title small{display:block;margin:6px 0 0}
.blogs{top:3130px;left:130px;display:flex;gap:20px}
.bcard{width:300px;height:280px;background:#fff;border-radius:4px;overflow:hidden;box-shadow:0 3px 12px rgba(0,0,0,.05)}
.bthumb{height:170px;background:linear-gradient(180deg,#f4e4c7 0%,#c9a88a 55%,#6d5a4d 100%)}
.bbody{padding:12px 16px;font-size:11px;line-height:1.7}
.bbody .date{color:var(--mute);font-size:10px}

.chat{top:3600px;left:130px;width:940px;height:170px;background:linear-gradient(90deg,#ffe27a,#fbc531);border-radius:6px}
.chat-photo{left:30px;top:-30px;width:170px;height:200px;border-radius:4px;background:linear-gradient(160deg,#f7d2c0,#e8a27c)}
.chat-text{left:250px;top:34px}
.chat-text h3{font-size:30px;font-weight:900}
.chat-text h3 em{font-style:normal;color:var(--red)}
.chat-text p{margin-top:6px;font-size:14px}
.chat .btn{position:absolute;right:30px;bottom:24px;height:40px}

.qa-head{top:3900px;left:60px}
.qa-head .sec-title small{display:block;margin:8px 0 0}
.qlist{top:3950px;left:520px;width:620px}
.q{height:88px;background:#fff;border-radius:4px;margin-bottom:24px;display:flex;align-items:center;padding:0 24px;font-size:13px;box-shadow:0 3px 12px rgba(0,0,0,.04);position:relative}
.q .mk{width:28px;height:28px;border-radius:50%;background:#fbe3de;color:var(--red);font-weight:800;font-family:"Montserrat",sans-serif;display:flex;align-items:center;justify-content:center;font-size:12px;margin-right:20px;flex:none}
.q .go{margin-left:auto;width:22px;height:22px;border-radius:50%;background:var(--red);position:relative;flex:none}
.q.ans{background:#fff8f6;border:1px solid #f6c9bf}
.q.ans .mk{background:var(--red);color:#fff}

.footer{top:4540px;left:0;width:1200px;height:244px;background:linear-gradient(90deg,var(--red),var(--orange) 60%,#f8a33a);color:#fff;text-align:center}
.footer .brand{justify-content:center;color:#fff;margin-top:40px;font-size:22px}
.footer .brand-dot{background:#fff}
.fnav{margin-top:34px;display:flex;justify-content:center;gap:32px;font-size:12px}
.fnav.sub{margin-top:18px;font-size:11px;opacity:.9}
.copy{margin-top:26px;font-size:10px;opacity:.85}
.deco{border-radius:50%}
</style>
</head>
<body>

<header class="site-header abs">
  <div class="brand"><span class="brand-dot"></span>ムーンホロウクラブ</div>
  <nav class="gnav"><span class="on">ホーム</span><span>Moonhollow Clubとは</span><span>講師紹介</span><span>ブログ</span><span>会員登録</span><span>よくある質問</span><span>お問い合わせ</span></nav>
  <span class="hbtn login">ログイン</span>
  <span class="hbtn join">会員登録はこちら</span>
</header>

<svg class="abs hero-ring" viewBox="0 0 760 760" aria-hidden="true">
  <defs>
    <linearGradient id="ring" x1="0" y1="0" x2="1" y2="1">
      <stop offset="0" stop-color="#fbe6e2"/>
      <stop offset=".45" stop-color="#e8352b"/>
      <stop offset=".8" stop-color="#f57a2a"/>
      <stop offset="1" stop-color="#fbc531"/>
    </linearGradient>
  </defs>
  <circle cx="380" cy="380" r="300" fill="none" stroke="url(#ring)" stroke-width="120" opacity=".92"/>
</svg>
<span class="abs deco" style="top:120px;left:1080px;width:14px;height:14px;background:var(--yellow)"></span>
<span class="abs deco" style="top:560px;left:400px;width:10px;height:10px;background:var(--red)"></span>

<div class="abs catch">
  <p><span class="big">個</span>性的な道を究め、</p>
  <p>劇的に生きる<span class="big">人生</span>を選択する</p>
  <p class="brand-line">それが<b>MOONHOLLOW</b></p>
</div>

<div class="abs photo" role="img" aria-label="前を見つめる女性の写真" style="top:700px;left:0;width:150px;height:160px;background:linear-gradient(160deg,#d9dde4,#9aa0ab)"></div>
<div class="abs photo" role="img" aria-label="赤い本を読む人の写真" style="top:720px;left:250px;width:190px;height:200px;background:linear-gradient(150deg,#f2e2d6,#d2463c)"></div>
<div class="abs photo" role="img" aria-label="ミーティングをする人々の写真" style="top:730px;left:760px;width:160px;height:150px;background:linear-gradient(150deg,#e6e2de,#a79a90)"></div>
<div class="abs photo" role="img" aria-label="パソコンで作業する人の写真" style="top:770px;left:1000px;width:200px;height:150px;background:linear-gradient(150deg,#d7d9dc,#7e838b)"></div>
<div class="abs dream en">Make Your Dreams Come True.</div>

<section class="abs about">
  <h2><span class="en">M<span>OONHOLLOW</span> C<span>LUB</span></span> とは</h2>
  <div class="bubble">あなたの<em>好き</em>なことは何ですか?</div>
  <p class="lead">好きなことを徹底追求し、“好き”を個性に。<br>そして、個性を武器にしながら“才能”へと伸ばしていくことで、<br>人生の構想力が磨かれ、あなたの人生は切り拓かれていきます。</p>
  <p class="lead">誰かに敷かれたレールに乗りたいのか?<br>型にはまらない人生を創造したいのか?<br>一度きりの人生を、自分はどう生きたいか?</p>
  <div class="claim">「自分らしい」人生を実現しよう!</div><br>
  <span class="btn">詳しく見る ›</span>
  <div class="abs city" role="img" aria-label="街並みのイラスト"></div>
</section>

<nav class="abs quick">
  <a><span class="ic"></span>ONLINE SALONでできること<span class="go"></span></a>
  <a><span class="ic"></span>講師の紹介<span class="go"></span></a>
  <a><span class="ic"></span>会員登録について<span class="go"></span></a>
  <a><span class="ic"></span>参加者の声<span class="go"></span></a>
</nav>

<h2 class="abs sec-title en" style="top:2400px;left:60px">Movie<small>新着動画</small></h2>
<div class="abs arrows"><span class="prev">←</span><span class="next">→</span></div>
<div class="abs movies">
  <article class="mcard"><div class="mthumb" role="img" aria-label="講義動画のサムネイル"><span class="tag">カテゴリー名が入ります</span><span class="play"></span></div><div class="mbody"><div class="cat">● 動画カテゴリー</div><div class="ttl">動画タイトルが入ります動画タイトルが入ります動画タイトル</div><div class="meta"><span><i></i>講師名</span><span>2021.04.01</span></div></div></article>
  <article class="mcard"><div class="mthumb" role="img" aria-label="講義動画のサムネイル"><span class="tag">カテゴリー名が入ります</span><span class="play"></span></div><div class="mbody"><div class="cat">● 動画カテゴリー</div><div class="ttl">動画タイトルが入ります動画タイトルが入ります動画タイトル</div><div class="meta"><span><i></i>講師名</span><span>2021.04.01</span></div></div></article>
  <article class="mcard"><div class="mthumb" role="img" aria-label="講義動画のサムネイル"><span class="tag">カテゴリー名が入ります</span><span class="play"></span></div><div class="mbody"><div class="cat">● 動画カテゴリー</div><div class="ttl">動画タイトルが入ります動画タイトルが入ります動画タイトル</div><div class="meta"><span><i></i>講師名</span><span>2021.04.01</span></div></div></article>
  <article class="mcard"><div class="mthumb" role="img" aria-label="講義動画のサムネイル"><span class="tag">カテゴリー名が入ります</span><span class="play"></span></div><div class="mbody"><div class="cat">● 動画カテゴリー</div><div class="ttl">動画タイトルが入ります動画タイトルが入ります動画タイトル</div><div class="meta"><span><i></i>講師名</span><span>2021.04.01</span></div></div></article>
</div>
<span class="abs btn ghost" style="top:2830px;left:60px">動画一覧を見る ›</span>

<div class="abs blog-head"><h2 class="sec-title en">Blog<small>ブログ</small></h2></div>
<div class="abs blogs">
  <article class="bcard"><div class="bthumb" role="img" aria-label="夕暮れの線路の写真"></div><div class="bbody"><div class="date">2021.04.01</div>タイトルが入りますタイトルが入りますタイトルが入りますタイトルが入ります</div></article>
  <article class="bcard"><div class="bthumb" role="img" aria-label="夕暮れの線路の写真"></div><div class="bbody"><div class="date">2021.04.01</div>タイトルが入りますタイトルが入りますタイトルが入りますタイトルが入ります</div></article>
  <article class="bcard"><div class="bthumb" role="img" aria-label="夕暮れの線路の写真"></div><div class="bbody"><div class="date">2021.04.01</div>タイトルが入りますタイトルが入りますタイトルが入りますタイトルが入ります</div></article>
</div>
<span class="abs btn ghost" style="top:3460px;left:520px">ブログ一覧を見る ›</span>

<section class="abs chat">
  <div class="abs chat-photo" role="img" aria-label="笑顔で話す女性の写真"></div>
  <div class="abs chat-text"><h3><em>自由</em>に<em>トーク</em>しませんか?</h3><p>誰もが自由に参加できるチャットルームです。気軽なことを仲間に共有しよう!</p></div>
  <span class="btn">チャットルームをご利用はこちらから ›</span>
</section>

<div class="abs qa-head"><h2 class="sec-title en">Q&amp;A<small>よくあるご質問</small></h2></div>
<div class="abs qlist">
  <div class="q"><span class="mk">Q</span>質問が入ります質問が入ります質問が入ります質問が入ります<span class="go"></span></div>
  <div class="q ans"><span class="mk">A</span>回答が入ります回答が入ります回答が入ります回答が入ります</div>
  <div class="q"><span class="mk">Q</span>質問が入ります質問が入ります質問が入ります質問が入ります<span class="go"></span></div>
  <div class="q"><span class="mk">Q</span>質問が入ります質問が入ります質問が入ります質問が入ります<span class="go"></span></div>
</div>
<span class="abs btn ghost" style="top:4470px;left:760px">もっと見る ›</span>

<footer class="abs footer">
  <div class="brand"><span class="brand-dot"></span>ムーンホロウクラブ</div>
  <nav class="fnav"><span>ホーム</span><span>Moonhollow Clubとは</span><span>講師紹介</span><span>ブログ</span><span>会員登録</span><span>よくある質問</span><span>お問い合わせ</span></nav>
  <nav class="fnav sub"><span>個人情報保護方針</span><span>特定商取引法に基づく表記</span><span>利用規約</span></nav>
  <p class="copy en">Copyright © Moonhollow Club All rights reserved.</p>
</footer>

</body>
</html>
```